Create a Flyer for switching service Power Falcon based on content

For a promo action for energy supplier switching service. With this flyer we are interested in our customers. The flyer should be in a detailed ppt, ie in an editable format, as we want to be able to include time, date and location specific text later (eg, this promo is for company A / B / C It should also be close to Pflcn's Corporate Design of Energy, accessible at https://powerfalcon-demo.at as, we added logo and designfile to the briefing to help you save time, these are also attached

Target Market(s)

Target Audience are Austrian homeowners or renters, who are in charge of buying electricity and gas. The brochure specifically targets them through their employee represenatives and / or HR departments.

Font styles to use
Sans Serif

Requirements
Must have
• It must be acceptable so we can include specifics for each given company and add contact details landing pages we will create for the specific company representatives.
Nice to have
• Different color schemes, any graphics around saving money,
Should not have
• We do not want to see pictures of real life people included in the design, as we prefer to follow the style of our homepage.

```html
<!DOCTYPE html>
<html lang="de">
<head>
<meta charset="utf-8">
<title>Power Falcon – Flyer Betriebsrat Aktion</title>
<link href="https://fonts.googleapis.com/css2?family=Montserrat:wght@600;700;800&family=Open+Sans:wght@400;600;700&display=swap" rel="stylesheet">
<style>
:root{
  --teal:#18a497;
  --teal-dark:#0f857a;
  --orange:#f5a11c;
  --ink:#3d3d3d;
  --muted:#6b6b6b;
  --paper:#ffffff;
  --stage:#eef0f2;
}
*{box-sizing:border-box;margin:0;padding:0}
html,body{width:1200px;height:3080px;overflow:hidden}
body{background:var(--stage);font-family:"Open Sans",Arial,sans-serif;color:var(--ink);
  display:flex;flex-direction:column;justify-content:space-evenly;align-items:center}
.spread{width:1200px;height:848px;display:flex;background:var(--paper);box-shadow:0 6px 24px rgba(0,0,0,.12)}
.panel{position:relative;width:400px;height:848px;overflow:hidden;padding:44px 38px;font-size:13px;line-height:1.55}
.panel + .panel{border-left:1px solid #e4e4e4}
h2,h3{font-family:"Montserrat",Arial,sans-serif;font-weight:800;text-transform:uppercase;line-height:1.25}
h2{font-size:16px;margin-bottom:12px}
h3{font-size:14px;margin:18px 0 8px}
p{margin-bottom:10px}
.accent{color:var(--orange);font-weight:700}
.teal-text{color:var(--teal)}
.shape{position:absolute;inset:0;width:100%;height:100%}
.layer{position:relative}
/* outside */
.company{position:absolute;left:38px;bottom:60px;font-size:13px}
.company h3{color:var(--teal);margin:0 0 8px}
.brand{display:flex;align-items:center;justify-content:flex-end;gap:8px;font-family:"Montserrat",Arial,sans-serif;font-weight:800;font-size:30px;color:var(--teal);letter-spacing:-.5px}
.brand-dot{width:16px;height:16px;border-radius:50%;background:var(--orange)}
.tagline{text-align:right;font-size:10px;color:var(--muted);margin-top:2px}
.offer-box{background:var(--teal);color:#fff;font-family:"Montserrat",Arial,sans-serif;font-weight:700;font-size:13px;text-transform:uppercase;padding:12px 14px;margin:34px 0 0 30px;line-height:1.4}
.hero-art{width:250px;height:250px;border-radius:50%;margin:34px auto 0;background:radial-gradient(circle at 50% 40%,#e9f6f3 0%,#bfe4dc 55%,#8fcfc2 100%)}
.promise{position:absolute;left:0;right:0;top:600px;color:#fff;font-weight:700;font-size:12px;padding:0 40px 0 120px;text-align:right}
.web-band{position:absolute;left:0;right:0;bottom:0;height:90px;background:var(--teal);color:#fff;font-family:"Montserrat",Arial,sans-serif;font-weight:700;font-size:19px;display:flex;align-items:center;justify-content:center;letter-spacing:.5px}
/* inside */
.drone-art{height:210px;margin:-44px -38px 18px;background:linear-gradient(180deg,#ffffff 0%,#e6f4f1 100%)}
.inside-left h2{color:var(--teal)}
.inside-left h3{color:var(--teal)}
ul.ticks{list-style:none;margin:4px 0 10px}
ul.ticks li{padding-left:18px;position:relative;margin-bottom:3px}
ul.ticks li::before{content:"";position:absolute;left:2px;top:6px;width:8px;height:4px;border-left:2px solid var(--orange);border-bottom:2px solid var(--orange);transform:rotate(-45deg)}
.hero-note{color:var(--teal);font-weight:700}
.inside-mid{background:var(--orange);color:#fff}
.inside-mid h2{color:#fff}
.mid-box{background:var(--teal);color:#fff;padding:16px 18px;margin-top:18px;font-weight:600}
.inside-right h2,.inside-right h3{color:var(--teal)}
.bulb-band{position:absolute;left:0;right:0;bottom:0;height:120px;background:var(--teal);display:flex;align-items:center;justify-content:space-between;padding:0 30px;color:#fff;font-family:"Montserrat",Arial,sans-serif;font-weight:700;font-size:18px}
.bulb-art{width:70px;height:90px;border-radius:50% 50% 40% 40%;background:radial-gradient(circle at 50% 40%,#ffe6a8,#f5a11c)}
</style>
</head>
<body>

<section class="spread outside">
  <div class="panel outside-left">
    <h2 class="teal-text">Wunschbedingungen</h2>
    <p>Power Falcon prüft Ihre Tarife laufend und informiert Sie, sobald ein günstigeres Angebot verfügbar ist. Sie entscheiden selbst, welche Bedingungen Ihnen wichtig sind.</p>
    <p class="accent">Ökostrom, Preisgarantie, regionale Anbieter.</p>
    <p>Unabhängig, transparent und ohne versteckte Kosten: Wir wechseln für Sie und kümmern uns um alle Formalitäten mit Ihrem alten und neuen Versorger.</p>
    <p class="accent">Kein Aufwand, keine Unterbrechung.</p>
    <p>Wer sich einmal anmeldet, bleibt automatisch beim besten Tarif. So sparen Haushalte jedes Jahr bares Geld bei Strom und Gas.</p>
    <p class="accent">Jetzt registrieren und profitieren.</p>
  </div>

  <div class="panel outside-mid">
    <svg class="shape" viewBox="0 0 400 848" preserveAspectRatio="none" aria-hidden="true">
      <polygon points="0,0 400,0 400,430 0,520" fill="var(--teal)"/>
    </svg>
    <div class="company">
      <h3>Nordwind Digital GmbH</h3>
      <p>Musterstraße 12<br>1010 Wien<br>+43 1 234 56 78<br>hallo@powerfalcon-demo.at</p>
    </div>
  </div>

  <div class="panel outside-cover">
    <svg class="shape" viewBox="0 0 400 848" preserveAspectRatio="none" aria-hidden="true">
      <polygon points="0,150 400,110 400,260 0,300" fill="var(--orange)"/>
      <polygon points="0,560 400,520 400,758 0,758" fill="var(--orange)"/>
    </svg>
    <div class="layer">
      <div class="brand">Power Falcon<span class="brand-dot"></span></div>
      <div class="tagline">Der automatische Tarifwechsel</div>
      <div class="offer-box">Betriebsrat Aktion Talwerk Kreditbank<br>10% Rabatt auf Ihren Wechsel</div>
      <div class="hero-art" role="img" aria-label="Illustration: Haus mit Windrädern und Solarpanelen in einem Kreis"></div>
    </div>
    <p class="promise">Einmal anmelden und dauerhaft beim günstigsten Anbieter bleiben.</p>
    <div class="web-band">www.powerfalcon-demo.at</div>
  </div>
</section>

<section class="spread inside">
  <div class="panel inside-left">
    <div class="drone-art" role="img" aria-label="Illustration: Drohnen tragen Glühbirnen über den Himmel"></div>
    <h2>Nur wer laufend wechselt, spart immer</h2>
    <p>Energiepreise ändern sich ständig. Mit Power Falcon bleiben Sie stets beim günstigsten Tarif:</p>
    <ul class="ticks">
      <li>automatische Tarifprüfung</li>
      <li>Wechsel ohne Aufwand</li>
      <li>persönliche Beratung</li>
    </ul>
    <h3>Betriebsrat Aktion Talwerk Kreditbank</h3>
    <p>Mitarbeitende erhalten 10% Rabatt auf die Servicegebühr im ersten Jahr.</p>
    <h3>Power Falcon</h3>
    <p class="hero-note">Jetzt anmelden unter powerfalcon-demo.at/aktion</p>
  </div>

  <div class="panel inside-mid">
    <h2>Wie funktioniert der Wechsel?</h2>
    <p>Sie registrieren sich online in wenigen Minuten und laden Ihre letzte Jahresabrechnung hoch.</p>
    <p>Wir vergleichen alle Anbieter in Österreich und wählen den Tarif, der zu Ihren Wünschen passt.</p>
    <p>Den Wechsel erledigen wir vollständig für Sie, inklusive Kündigung beim bisherigen Versorger.</p>
    <p>Jedes Jahr prüfen wir erneut und wechseln wieder, sobald sich eine Ersparnis ergibt.</p>
    <div class="mid-box">Power Falcon ist unabhängig und erhält keine Provisionen von Energieanbietern. Ihr Vorteil steht immer im Mittelpunkt.</div>
  </div>

  <div class="panel inside-right">
    <h2>Welche Vorteile als Power Falcon Wechselkunde?</h2>
    <p><span class="accent">Ersparnis:</span> Im Schnitt sparen Haushalte mehrere hundert Euro pro Jahr.</p>
    <p><span class="accent">Sicherheit:</span> Ihre Versorgung läuft ohne Unterbrechung weiter.</p>
    <p><span class="accent">Komfort:</span> Keine Formulare, keine Fristen, kein Aufwand.</p>
    <p><span class="accent">Service:</span> Persönliche Ansprechpartner bei allen Fragen.</p>
    <h3>Zum Unternehmen selbst</h3>
    <p>Power Falcon wurde in Wien gegründet und betreut tausende Haushalte beim Strom- und Gaswechsel in ganz Österreich.</p>
    <div class="bulb-band">
      <span>www.powerfalcon-demo.at</span>
      <div class="bulb-art" role="img" aria-label="Illustration: leuchtende Glühbirne"></div>
    </div>
  </div>
</section>

</body>
</html>
```